Briefpapier im Word-Format für Sachverständigenbüro
Zielgruppe
Sachverständigenbüro für Sach- und Haftpflichtversicherungsschäden
Aufgabenstellung
Beibehaltung aktueller Logos, Erstellung einer Word-Datei zum selbst ausdrucken und kompatibel für Ausdruck über Word ohne Abschnitt der Seitenränder

```html
<!DOCTYPE html>
<html lang="de">
<head>
<meta charset="utf-8">
<title>Briefpapier – Gutachterbüro Weidental</title>
<link rel="stylesheet" href="https://fonts.googleapis.com/css2?family=Open+Sans:wght@400;600&family=Fira+Sans:wght@400&display=swap">
<style>
  :root {
    --backdrop: #d3d3d3;
    --paper: #fdfdfd;
    --brand-red: #c8161d;
    --ink: #3a3a3a;
    --ink-soft: #555;
    --ink-muted: #6a6a6a;
  }
  * { box-sizing: border-box; margin: 0; padding: 0; }
  html, body { width: 1166px; height: 1200px; overflow: hidden; }
  body {
    background: var(--backdrop);
    font-family: "Open Sans", Arial, sans-serif;
    color: var(--ink);
  }
  .letterhead {
    position: absolute;
    left: 187px; top: 40px;
    width: 792px; height: 1120px;
    background: var(--paper);
    box-shadow: 0 6px 18px rgba(0,0,0,.12);
  }
  .header-rule {
    position: absolute; left: 480px; top: 80px;
    width: 240px; height: 5px; background: var(--brand-red);
  }
  .brand-name {
    position: absolute; left: 480px; top: 98px;
    font-size: 19px; font-weight: 600; letter-spacing: .5px;
    color: var(--ink);
  }
  .sender-line {
    position: absolute; left: 80px; top: 220px;
    font-size: 9px; text-decoration: underline; color: #111;
  }
  .sender-line .accent { color: var(--brand-red); }
  .recipient {
    position: absolute; left: 80px; top: 240px;
    font-size: 13px; line-height: 19px; color: var(--ink-soft);
  }
  .letter-body {
    position: absolute; left: 80px; top: 380px; width: 620px;
    font-size: 12.5px; line-height: 19px; color: var(--ink-soft);
  }
  .letter-body p { margin-bottom: 14px; }
  .footer {
    position: absolute; left: 60px; right: 60px; bottom: 60px;
    font-family: "Fira Sans", Arial, sans-serif;
    font-size: 11px; line-height: 15px; color: var(--ink-muted);
  }
  .footer-rule { height: 1.5px; background: var(--brand-red); }
  .footer-columns {
    display: flex; justify-content: space-between; padding: 10px 0;
  }
  .footer-columns div:nth-child(3) { padding-top: 10px; }
  .footer-columns div:nth-child(4) { padding-top: 22px; }
</style>
</head>
<body>
  <article class="letterhead">
    <div class="header-rule"></div>
    <div class="brand-name">Gutachterbüro Weidental</div>

    <div class="sender-line">Gutachterbüro <span class="accent">Weidental |</span> Lindenhof 8 <span class="accent">|</span> 86999 Kornfeld</div>

    <address class="recipient" style="font-style:normal">
      Mustermann GmbH<br>
      Herr Max mustermann<br>
      Musterstraße 4711<br>
      08159 Musterstadt
    </address>

    <section class="letter-body">
      <p>Lorem ipsum dolor sit amet, consetetur sadipscing elitr, sed diam nonumy eirmod tempor invidunt ut labore et dolore magna aliquyam erat, sed diam voluptua. At vero eos et accusam et justo duo dolores et ea rebum. Stet clita kasd gubergren, no sea takimata sanctus est Lorem psum dolor sit amet.</p>
      <p>Lorem ipsum dolor sit amet, consetetur sadipscing elitr, sed diam nonumy eirmod tempor invidunt ut labore et dolore magna aliquyam erat, sed diam voluptua. At vero eos et accusam et justo duo dolores et ea rebum. Stet clita kasd gubergren, no sea takimata s anctus est Lorem ipsum dolor sit amet. Lorem ipsum dolor sit amet, consetetur sadipscing elitr, sed diam nonumy eirmod tempor.</p>
      <p>invidunt ut labore et dolore magna aliquyam erat, sed diam voluptua. At vero eos et accusam et justo duo dolores et ea rebum. Stet clita kasd gubergren, no sea takimata sanctus est Lorem psum dolor sit amet. Lorem ipsum dolor sit amet, consetetur sadipscing elitr, sed diam nonumy eirmod tempor invidunt ut labore et dolore magna aliquyam erat, sed diam voluptua.</p>
      <p>At vero eos et accusam et justo duo dolores et ea rebum. Stet clita kasd gubergren, no sea takimata s anctus est Lorem ipsum dolor sit amet.</p>
    </section>

    <footer class="footer">
      <div class="footer-rule"></div>
      <div class="footer-columns">
        <div>Gutachterbüro Weidental<br>Finkenstieg 4<br>86999 Kornfeld</div>
        <div>Inhaber: Jonas Brettmaier<br>E-Mail: info@weidental-gutachten.de<br>Internet: www.weidental-gutachten.de</div>
        <div>Tel: 01234 / 567801<br>Fax: 01234 / 567802<br>Terminhotline: 0170 / 9988776</div>
        <div>USt ID DE000111222<br>IBAN: DE00123456780000123456<br>BIC: GENODEF0XYZ</div>
      </div>
      <div class="footer-rule"></div>
    </footer>
  </article>
</body>
</html>
```